GuardVOLT Brochure

We need a new brochure designed for our GuardVOLT Unit. I have provided examples of previous and words for the new ones. Stock photos will be purchased and forwarded once design is complete.

I have also attached a competitors product brochure for reference. This is a bout conveying by using our product your people will be safe and will not need to use high rated PPE
Updates

Project Deadline Extended
Reason: Will be extending the project for 1 day and selecting the final design tomorrow to allow some of you to fine tune submissions.

Target Market(s)

Professionals

Industry/Entity Type

Product

Contact Information for Business Card

Refer Attached Details

Requirements
Must have
• Pemberton Lisle Logo and Colours Business Card
• Brochure should complement GuardVOLT Logo

```html
<!DOCTYPE html>
<html lang="en">
<head>
<meta charset="utf-8">
<title>Product Brochure Spread</title>
<link href="https://fonts.googleapis.com/css2?family=Lato:wght@400;700&family=Arimo:wght@400;700&display=swap" rel="stylesheet">
<style>
  :root {
    --stage: #d8d3cb;
    --blue: #17629e;
    --white: #ffffff;
    --red: #c4163c;
    --panel-top: #e4e6ef;
    --panel-bottom: #ffffff;
    --grid: #c9ccd4;
    --ink: #222;
    --navy: #1f2a66;
    --orange: #e8661f;
    --green: #7bb342;
    --purple: #5b3fa8;
    --cyan: #2fb3d6;
    --curve-red: #c4161c;
    --copper-dark: #7a3f1c;
    --copper-light: #c27a45;
  }
  * { margin: 0; padding: 0; box-sizing: border-box; }
  html, body { width: 1200px; height: 795px; overflow: hidden; background: var(--stage); }
  .spread { position: absolute; left: 38px; top: 0; width: 1124px; height: 795px; display: flex; }
  .panel { position: relative; width: 562px; height: 795px; overflow: hidden; }
  .panel--left { background: var(--blue); color: var(--white); font-family: "Arimo", Arial, sans-serif; }
  .panel--right { background: linear-gradient(180deg, var(--panel-top), var(--panel-bottom) 70%); }
  .burst-glow { position: absolute; left: 220px; top: -40px; width: 260px; height: 260px; border-radius: 50%;
    background: radial-gradient(circle, rgba(255,255,255,0.14), rgba(255,255,255,0) 70%); }
  .bolt-glow { position: absolute; left: 10px; top: 0; width: 140px; height: 240px;
    background: linear-gradient(160deg, rgba(196,22,60,0.12), rgba(196,22,60,0) 75%); }
  .content { position: absolute; left: 66px; width: 250px; }
  .heading { font-family: "Lato", sans-serif; font-weight: 400; font-size: 17px; line-height: 20px; }
  .heading--large { font-size: 21.5px; line-height: 26px; }
  .subhead { font-weight: 700; font-size: 11.5px; line-height: 14px; }
  ul, ol { list-style: none; font-size: 11.5px; line-height: 17px; }
  li { position: relative; padding-left: 16px; }
  ul li::before { content: "•"; position: absolute; left: 2px; }
  ol { counter-reset: n; }
  ol li { counter-increment: n; }
  ol li::before { content: counter(n) "."; position: absolute; left: 0; }
  .ordinal { font-size: 7px; line-height: 0; vertical-align: 4px; }
  .arc-list { width: 430px; }
  .body-copy { font-size: 11.5px; line-height: 17px; text-align: justify; width: 243px; }
  .standards li { line-height: 20px; }
  .tests li { line-height: 17.3px; }
  .product-photo { position: absolute; left: 300px; top: 430px; width: 262px; height: 365px;
    background: linear-gradient(135deg, var(--copper-light), var(--copper-dark));
    clip-path: polygon(22% 0, 100% 0, 100% 100%, 12% 100%, 12% 50%, 0 46%, 0 30%, 10% 28%, 10% 8%); }
  .chart-title { position: absolute; left: 93px; font-family: "Lato", sans-serif; font-weight: 400; color: var(--red); font-size: 15px; line-height: 18px; }
  .charts { position: absolute; left: 0; top: 0; font-family: "Arimo", Arial, sans-serif; }
</style>
</head>
<body>
<div class="spread">
  <section class="panel panel--left">
    <div class="burst-glow"></div>
    <div class="product-photo" role="img" aria-label="Photo of the switchgear cabinet in copper finish"></div>

    <h2 class="heading content" style="top:82px">The Arc Flash Problem</h2>
    <ul class="content arc-list" style="top:107px">
      <li>Heat causes 2<span class="ordinal">nd</span> degree burns on exposed skin;</li>
      <li>Heat ignites clothing causing severe 3<span class="ordinal">rd</span> degree burns;</li>
      <li>Inhaling of molten metal and the toxic plasma plume causes lung damage;</li>
      <li>Pressure wave sound can exceed levels which can damage human ears;</li>
      <li>Pressure wave can cause personnel injury.</li>
    </ul>
    <p class="subhead content" style="top:205px">Most arc flash events are caused by:</p>
    <ol class="content" style="top:221px">
      <li>Human error.</li>
      <li>Equipment failure;</li>
      <li>Vermin Infestation.</li>
    </ol>
    <p class="subhead content" style="top:289px">The severity factors involved are:</p>
    <ol class="content" style="top:310px;width:300px">
      <li>Energy, how big is the explosion;</li>
      <li>Time, how long does the explosion go for;</li>
    </ol>

    <h2 class="heading heading--large content" style="top:386px">Safety is Important, Need Further Proof Right?</h2>
    <p class="body-copy content" style="top:458px">Type testing was performed by the Corvane, Velmar certified test center located in Melbourne Victoria Australia during June 2010 through to September 2012. The testing program was conducted in accordance with:</p>
    <ul class="content standards" style="top:545px;width:250px">
      <li>AS\IEC60947.1 Low Voltage Switchgear and Control Gear – General Rules; and</li>
      <li>AS3439.1 Low Voltage Switchgear and Control Gear Assemblies</li>
    </ul>
    <p class="subhead content" style="top:637px">The tests performed included:</p>
    <ul class="content tests" style="top:653px">
      <li>Short Circuit Test;</li>
      <li>TCC Validation;</li>
      <li>Dielectric Tests;</li>
      <li>Temperature Rise; and</li>
      <li>Arc Fault Containment.</li>
    </ul>
  </section>

  <section class="panel panel--right">
    <div class="bolt-glow"></div>
    <h3 class="chart-title" style="top:76px">Time- Current Curve, 3200A Unit @415V 50Hz</h3>
    <h3 class="chart-title" style="top:444px">Peak Let Through Curve 3200A Unit @415V 50Hz</h3>

    <svg class="charts" width="562" height="795" viewBox="0 0 562 795" aria-label="Fuse performance charts">
      <g stroke="var(--grid)" stroke-width="0.6" fill="none">
        <rect x="144" y="115" width="235" height="270" fill="#fff"/>
        <path d="M180 115V385M200 115V385M215 115V385M226 115V385M235 115V385M243 115V385M249 115V385M255 115V385M261 115V385
                 M297 115V385M317 115V385M332 115V385M343 115V385M352 115V385M360 115V385M366 115V385M372 115V385"/>
        <path d="M144 139.5H379M144 164H379M144 188.5H379M144 213H379M144 238H379M144 262.5H379M144 287H379M144 311.5H379M144 336H379M144 360.5H379"/>
      </g>
      <g font-size="5.5" fill="var(--ink)" text-anchor="end">
        <text x="139" y="117">1000000</text><text x="139" y="141.5">100000</text><text x="139" y="166">10000</text>
        <text x="139" y="190.5">1000</text><text x="139" y="215">100</text><text x="139" y="240">10</text>
        <text x="139" y="264.5">1</text><text x="139" y="289">0.1</text><text x="139" y="313.5">0.01</text>
        <text x="139" y="338">0.001</text><text x="139" y="362.5">0.0001</text><text x="139" y="387">0.00001</text>
      </g>
      <g font-size="5.5" fill="var(--ink)" text-anchor="middle">
        <text x="144" y="393">1000</text><text x="261" y="393">10000</text><text x="379" y="393">100000</text>
        <text x="261" y="402" font-weight="700" font-size="5">Prospective Current in Amperes RMS</text>
      </g>
      <text transform="translate(117 250) rotate(-90)" font-size="5" font-weight="700" text-anchor="middle" fill="var(--ink)">Virtual Pre-Arcing Time in Seconds</text>
      <g fill="none" stroke-width="1.2">
        <path d="M202 115V140" stroke="var(--purple)"/>
        <path d="M202 140L230 200L255 238L270 256" stroke="var(--green)"/>
        <path d="M218 178L244 227L265 255L270 302L275 311L289 319L368 357" stroke="var(--curve-red)"/>
        <path d="M218 174L245 212L265 240L270 274L275 307L284 314L354 320" stroke="var(--orange)"/>
        <path d="M220 176L246 210L265 237L272 279L279 307L289 310L354 314" stroke="var(--cyan)"/>
      </g>
      <g font-size="4.8" fill="var(--ink)">
        <line x1="383" y1="142" x2="396" y2="142" stroke="var(--curve-red)"/>
        <text x="398" y="144"><tspan x="398">Calculated 3200A</tspan><tspan x="398" dy="6">Parallel Semi-</tspan><tspan x="398" dy="6">Conductor Fuse</tspan><tspan x="398" dy="6">Segment</tspan></text>
        <line x1="383" y1="188" x2="396" y2="188" stroke="var(--green)"/>
        <text x="398" y="190"><tspan x="398">Calculated 3200A</tspan><tspan x="398" dy="6">Parallel Semi-</tspan><tspan x="398" dy="6">Conductor Fuse</tspan><tspan x="398" dy="6">AA-Curve</tspan><tspan x="398" dy="6">Segment</tspan></text>
        <line x1="383" y1="234" x2="396" y2="234" stroke="var(--purple)"/>
        <text x="398" y="236"><tspan x="398">Calculated 3200A</tspan><tspan x="398" dy="6">Parallel Semi-</tspan><tspan x="398" dy="6">Conductor Fuse</tspan><tspan x="398" dy="6">Nominal Rating</tspan><tspan x="398" dy="6">(In) Segment</tspan></text>
        <line x1="383" y1="280" x2="396" y2="280" stroke="var(--orange)"/>
        <text x="398" y="282"><tspan x="398">3200A Parallel</tspan><tspan x="398" dy="6">Semi-Conductor</tspan><tspan x="398" dy="6">Fuse Test -</tspan><tspan x="398" dy="6">PreARC Results</tspan></text>
        <line x1="383" y1="326" x2="396" y2="326" stroke="var(--cyan)"/>
        <text x="398" y="328"><tspan x="398">3200A Parallel</tspan><tspan x="398" dy="6">Semi-Conductor</tspan><tspan x="398" dy="6">Fuse Test -</tspan><tspan x="398" dy="6">Clearing Results</tspan></text>
      </g>

      <g stroke="var(--grid)" stroke-width="0.6" fill="none">
        <rect x="127" y="484" width="293" height="201" fill="#fff"/>
        <path d="M156 484V685M174 484V685M186 484V685M195 484V685M203 484V685M210 484V685M215 484V685M220 484V685M225 484V685
                 M254 484V685M272 484V685M284 484V685M293 484V685M301 484V685M307 484V685M313 484V685M318 484V685M322 484V685
                 M352 484V685M369 484V685M381 484V685M391 484V685M398 484V685M405 484V685M411 484V685M416 484V685"/>
        <path d="M127 655H420M127 637H420M127 624H420M127 615H420M127 607H420M127 600H420M127 594H420M127 589H420M127 585H420
                 M127 554H420M127 536H420M127 524H420M127 514H420M127 506H420M127 499H420M127 494H420M127 489H420"/>
      </g>
      <g fill="none" stroke="var(--navy)" stroke-width="1.2">
        <path d="M127 644L287 484"/>
        <path d="M226 545L329 513"/>
        <path d="M329 513L420 485" stroke-dasharray="7 4"/>
      </g>
      <path d="M245 541L303 529" stroke="var(--orange)" stroke-width="1.2" fill="none"/>
      <g font-size="5.5" fill="var(--ink)">
        <text x="130" y="629">A</text><text x="268" y="491">B</text>
        <text x="122" y="487" text-anchor="end">100000</text>
        <text x="122" y="587" text-anchor="end">10000</text>
        <text x="122" y="687" text-anchor="end">1000</text>
        <text x="127" y="693" text-anchor="middle">1000</text><text x="225" y="693" text-anchor="middle">10000</text>
        <text x="322" y="693" text-anchor="middle">100000</text><text x="420" y="693" text-anchor="middle">1000000</text>
        <text x="273" y="702" font-size="5" font-weight="700" text-anchor="middle">Prospective Short-Circuit Current Symmetrical RMS</text>
      </g>
      <text transform="translate(103 585) rotate(-90)" font-size="5" font-weight="700" text-anchor="middle" fill="var(--ink)">Peak Let-Through Current</text>
      <g font-size="4.8" fill="var(--ink)">
        <line x1="425" y1="550" x2="437" y2="550" stroke="var(--navy)"/>
        <text x="439" y="552"><tspan x="439">Calculated 3200A</tspan><tspan x="439" dy="6">Parallel Semi-</tspan><tspan x="439" dy="6">Conductor Fuse</tspan><tspan x="439" dy="6">Segment</tspan></text>
        <line x1="425" y1="596" x2="437" y2="596" stroke="var(--orange)"/>
        <text x="439" y="598"><tspan x="439">3200A  Parallel</tspan><tspan x="439" dy="6">Semi-Conductor</tspan><tspan x="439" dy="6">Fuse Test Results</tspan></text>
      </g>
    </svg>
  </section>
</div>
</body>
</html>
```